Rockband need a complete CD package.

BRASSLANTERN Artwork
Artist: BRASSLANTERN
Title: The Tin Harbor
Format/Delivery:
- Digipack - Version with Booklet
- Cardboard Bag
- CD Design
- .psd/.psb (or similar) File with all Layers and Designs
- Social Media Banners
- High Resolution Files 300dpi/6000px to 6000px
We are a rock band and need artwork and booklet design for our new mini-album. We have attached the idea as a draft here. The following is important to us regarding this artwork design:
- The result should be as similar as the draft.
- We want to keep it light as in the draft, but it can have gray structures in it.
- It should be a little more contrasting than the draft.
- The band's original lettering is attached. This should be used.
- The lion's eye should be a bright red or a bright yellow/orange.
- The color of the eye should be the only color that appears repeatedly in the booklet and digipac design.
- The background can have crackles and other paintbrushes to give it a slightly used look.
- The booklet and digipack may be darker than the artwork (but don't have to be). So you can play around with black and white variations. The cover, on the other hand, should be as bright as in the draft.
- The CD design should be simple, without the album title or lettering.
- The logo is also attached and can be used if needed.
- On the cardboard bag should be printed a promotion QR Code (QR-Code will be sent during the job)
- In general: The artwork should radiate power, motivation, and liberation from the energy.
There will be 7 Tracks:
- Lanterns
- The Kettle
- Paper Boats
- Gardeners of Quiet Stones
- Clock Twister
- Their Slowest Noon
- The Color of The Well
The texts will be delivered during the project.

```html
<!DOCTYPE html>
<html lang="en">
<head>
<meta charset="utf-8">
<title>BRASSLANTERN – The Tin Harbor – Booklet Lyrics Spreads</title>
<link href="https://fonts.googleapis.com/css2?family=EB+Garamond:wght@400;600;700&display=swap" rel="stylesheet">
<style>
  :root {
    --backdrop: #c6cfd9;
    --page-dark: #2f2f2f;
    --page-mid: #4a4a4a;
    --page-light: #5a5a5a;
    --ink: #ecebe8;
    --ink-soft: #d9d8d4;
    --ink-ghost: rgba(236, 235, 232, 0.22);
    --rule: rgba(236, 235, 232, 0.45);
  }
  * { margin: 0; padding: 0; box-sizing: border-box; }
  html, body {
    width: 1196px; height: 1200px; overflow: hidden;
    background: var(--backdrop);
    font-family: "EB Garamond", Garamond, serif;
    color: var(--ink);
  }
  .spread {
    position: absolute; left: 160px; width: 857px; height: 429px;
    display: flex;
  }
  .spread--top { top: 147px; }
  .spread--bottom { top: 614px; }
  .page {
    position: relative; width: 50%; height: 100%;
    padding: 17px 23px 0 23px;
    background:
      radial-gradient(ellipse at 30% 20%, var(--page-light) 0%, transparent 60%),
      radial-gradient(ellipse at 75% 80%, var(--page-mid) 0%, transparent 65%),
      linear-gradient(160deg, var(--page-mid), var(--page-dark));
  }
  .page--left { box-shadow: inset -14px 0 18px -12px rgba(0,0,0,0.45); }
  .page--right { box-shadow: inset 14px 0 18px -12px rgba(0,0,0,0.45); }
  .song-title {
    font-weight: 700; font-size: 21px; line-height: 1.1; color: var(--ink);
  }
  .song-credit {
    font-size: 13px; line-height: 1.2; color: var(--ink-soft); margin-bottom: 9px;
  }
  .bpm {
    position: absolute; top: 16px; right: 16px;
    font-size: 7.5px; letter-spacing: 0.3px; color: var(--ink-soft);
  }
  .lyrics { font-size: 12.2px; line-height: 13.7px; color: var(--ink); }
  .lyrics p { margin-bottom: 13.7px; }
  .lyrics .ghost { color: var(--ink-ghost); }
  .lyrics--spaced { margin-top: 46px; }
  .lyrics--continued { margin-top: 0; }
  .folio {
    position: absolute; left: 23px; right: 17px; bottom: 9px;
    display: flex; align-items: center; gap: 6px;
    font-size: 13px; color: var(--ink-soft);
  }
  .folio::before {
    content: ""; flex: 1; height: 1px; background: var(--rule);
  }
</style>
</head>
<body>

<section class="spread spread--top">
  <article class="page page--left">
    <h1 class="song-title">Paper Boats</h1>
    <p class="song-credit">(music &amp; lyrics by brasslantern)</p>
    <span class="bpm">BPM: 105</span>
    <div class="lyrics lyrics--spaced">
      <p>Distant lands, foreign skies<br>I’ve roamed the earth with open eyes<br>Mountains high and oceans wide<br>Into the great divide.</p>
      <p>No matter where I’ve been<br>There is one thing I can’t pretend<br>It’s you I long to see<br><span class="ghost">Lanterns</span><br>I’m coming home, where I belong<br>To the ones who’ve made me strong<br>Every journey, every mile<br>I missed your smile<br>I’m coming home, where I belong<br>To the ones who’ve held me strong<br>Every journey, every mile<br>I missed your smile</p>
      <p>Crowded streets and city lights<br>I’ve chased my dreams through endless nights<br>In the silence of the unknown<br>I hear echoes of my own</p>
    </div>
    <div class="folio">05</div>
  </article>
  <article class="page page--right">
    <div class="lyrics lyrics--continued">
      <p>Through constant noise<br>Your love remained my steady voice<br>In the dark I’d hear you call<br><span class="ghost">Lanterns</span><br>I’m coming home, where I belong<br>To the ones who’ve made me strong<br>Every journey, every mile<br>I missed your smile<br>I’m coming home, where I belong<br>To the ones who’ve held me strong<br>Every journey, every mile<br>I missed your smile</p>
      <p>If I lose my way, the fire still burns every day<br>For the love that I find in your arms<br><span class="ghost">Towards a brand-new day</span><br>I’m coming home, where I belong<br>To the ones who’ve made me strong<br>Every journey, every mile<br>I missed your smile<br>I’m coming home, where I belong<br>To the ones who’ve held me strong<br>Every journey, every mile<br>I missed your smile</p>
    </div>
    <div class="folio">06</div>
  </article>
</section>

<section class="spread spread--bottom">
  <article class="page page--left">
    <h1 class="song-title">Gardeners Of Quiet Stones</h1>
    <p class="song-credit">(music &amp; lyrics by brasslantern)</p>
    <span class="bpm">BPM: 154</span>
    <div class="lyrics">
      <p>In the city of grey where the sidewalks meet the sky<br>Where all the love and passion’s gone – no goodbye<br>The clocks are ticking slowly, in this city full of routine<br>Each day is like the day before, and colors remain unseen</p>
      <p>In the heart of the young spirit, a rumor starts to rise<br>That the gardeners of quiet stones, in a world so black and white<br>Are yearning for a symphony where dreams and colors blend<br>Imagine a new beginning and the old world to end</p>
      <p>In the shadows of the buildings where echoes never cease<br>There’s a rebel with a heartbeat searching for release<br>The chains are finally breaking, hear the freedom ring<br>The anthem of rebellion – together we all sing</p>
      <p>In the heart of the young spirit, a rumor starts to rise<br>That the gardeners of quiet stones, in a world so black and white<br>Are yearning for a symphony where dreams and colors blend<br>Imagine a new beginning and the old world to end</p>
      <p>In the heart of the young spirit, a whisper starts to rise<br>From the gardeners of quiet stones, in a world so black and white<br>They long to hear a symphony where dreams and colors blend<br>Imagine a new beginning and the old world to end</p>
    </div>
    <div class="folio">07</div>
  </article>
  <article class="page page--right">
    <h1 class="song-title">Clock Twister</h1>
    <p class="song-credit">(music &amp; lyrics by brasslantern)</p>
    <span class="bpm">BPM: 111</span>
    <div class="lyrics">
      <p>Breathe in<br>Fill that empty space inside<br>Now breathe out<br>Free your cluttered mind</p>
      <p>Don’t you wonder if there’s still something around?</p>
      <p>Oh, shout it out<br>No, don’t give in<br>Take a look around – this ain’t everything<br>Don’t run for cover<br>Place your bets tonight<br>Shake off the demons that are messing with your mind</p>
      <p>Waste no time or time will waste you<br>Try to kill the noise that rings inside your head</p>
      <p>Don’t you wonder if there’s still someone around?<br>Oh, shout it out</p>
      <p>No, don’t give in<br>Take a look around – this ain’t everything<br>Don’t run for cover<br>Place your bets tonight<br>Shake off the demons that are messing with your mind</p>
    </div>
    <div class="folio">08</div>
  </article>
</section>

</body>
</html>
```